Crypto currency project website revamp

Our current website is: http://www.quillbarn.org

The new logo is also attached.

Here are some examples of the other crypto websites. Our goal is to re-make the above website to look and feel like the followings:

1) https://9tumbler.com/

2) https://varsk.io/

3) https://quorvale.network/#/

Please submit your designs. Once we found the right design we need to interate a bit and add 3 or 4 more sections to it.

The coded website needs to be responsive

```html
<!DOCTYPE html>
<html lang="en">
<head>
<meta charset="utf-8">
<title>Quillbarn — Decentralized Exchange Graph</title>
<link href="https://fonts.googleapis.com/css2?family=Exo+2:wght@400;500;600;700&display=swap" rel="stylesheet">
<style>
  :root {
    --white: #ffffff;
    --ink: #1c1f2b;
    --brand-blue: #1f6fd8;
    --hero-light: #eaf4fd;
    --hero-mid: #8cc6f2;
    --hero-deep: #3f8fe0;
    --magenta-dark: #7e1340;
    --magenta: #b81f57;
    --magenta-glow: #f05a8c;
    --yellow: #f2cf1f;
    --yellow-mid: #f8e468;
    --yellow-light: #fff6c4;
    --navy: #070d1c;
    --navy-mid: #1b2c52;
    --navy-glow: #3a5a92;
    --sky: #3fb8ec;
    --sky-deep: #1e8fd0;
    --sky-light: #c6efff;
    --footer: #2a2a2c;
    --footer-bar: #141415;
    --orange: #f47a20;
  }
  * { margin: 0; padding: 0; box-sizing: border-box; }
  html, body { width: 1200px; height: 2812px; overflow: hidden; }
  body { font-family: "Exo 2", sans-serif; color: var(--ink); background: var(--white); position: relative; }

  .site-header {
    position: absolute; top: 0; left: 0; width: 1200px; height: 60px;
    display: flex; align-items: center; justify-content: space-between;
    padding: 0 40px; z-index: 2;
  }
  .brand { display: flex; align-items: center; gap: 10px; font-weight: 600; font-size: 18px; letter-spacing: 2px; color: var(--brand-blue); }
  .brand-dot { width: 16px; height: 16px; border-radius: 50%; background: var(--brand-blue); }
  .main-nav { display: flex; gap: 34px; font-size: 14px; font-weight: 500; }
  .main-nav a { color: var(--ink); text-decoration: none; }

  .panel { position: absolute; left: 0; width: 1200px; overflow: hidden; }
  .panel-art { position: absolute; inset: 0; }
  .panel-copy { position: absolute; }
  .panel-copy h2 { font-size: 40px; font-weight: 600; line-height: 1.1; margin-bottom: 18px; letter-spacing: 1px; }
  .panel-copy p { font-size: 19px; line-height: 1.3; }

  .hero { top: 0; height: 560px; background: var(--white); }
  .hero-art {
    position: absolute; left: 0; top: 40px; width: 820px; height: 520px;
    background:
      radial-gradient(ellipse 180px 150px at 45% 70%, var(--hero-deep) 0%, transparent 100%),
      radial-gradient(ellipse 200px 130px at 20% 40%, var(--hero-mid) 0%, transparent 100%),
      radial-gradient(ellipse 160px 110px at 70% 35%, var(--hero-mid) 0%, transparent 100%),
      radial-gradient(ellipse at 40% 55%, var(--hero-mid) 0%, var(--hero-light) 60%, rgba(255,255,255,0) 85%);
  }
  .hero-copy { left: 688px; top: 352px; width: 470px; }
  .hero-copy h1 { font-size: 30px; font-weight: 700; letter-spacing: 3px; color: var(--brand-blue); margin-bottom: 6px; }
  .hero-copy p { font-size: 22px; line-height: 1.25; color: var(--brand-blue); }

  .peer { top: 560px; height: 510px; }
  .peer .panel-art {
    background:
      radial-gradient(ellipse 260px 200px at 70% 45%, var(--magenta-glow) 0%, transparent 100%),
      radial-gradient(ellipse 220px 160px at 88% 75%, var(--magenta-glow) 0%, transparent 100%),
      radial-gradient(ellipse 200px 140px at 55% 85%, #d63a72 0%, transparent 100%),
      linear-gradient(100deg, var(--magenta-dark) 0%, var(--magenta) 45%, #cf2c66 100%);
  }
  .peer .panel-copy { left: 80px; top: 160px; width: 480px; color: var(--white); }

  .fee { top: 1070px; height: 510px; }
  .fee .panel-art {
    background:
      radial-gradient(ellipse 260px 220px at 12% 40%, var(--yellow) 0%, transparent 100%),
      radial-gradient(ellipse 240px 180px at 30% 85%, var(--yellow-mid) 0%, transparent 100%),
      radial-gradient(ellipse 220px 160px at 85% 20%, var(--yellow-light) 0%, transparent 100%),
      linear-gradient(90deg, var(--yellow) 0%, var(--yellow-mid) 35%, var(--yellow-light) 70%, #fffbe8 100%);
  }
  .fee .panel-copy { left: 304px; top: 178px; width: 560px; color: var(--ink); }

  .currencies { top: 1580px; height: 520px; }
  .currencies .panel-art {
    background:
      radial-gradient(ellipse 220px 180px at 63% 42%, var(--navy-glow) 0%, transparent 100%),
      radial-gradient(ellipse 160px 120px at 45% 20%, var(--navy-mid) 0%, transparent 100%),
      radial-gradient(ellipse 160px 120px at 85% 30%, var(--navy-mid) 0%, transparent 100%),
      radial-gradient(ellipse at 65% 45%, var(--navy-mid) 0%, var(--navy) 70%);
  }
  .currencies .panel-copy { left: 80px; top: 280px; width: 440px; color: var(--white); }

  .bitlume { top: 2100px; height: 520px; }
  .bitlume .panel-art {
    background:
      radial-gradient(ellipse 260px 200px at 25% 40%, var(--sky-light) 0%, transparent 100%),
      radial-gradient(ellipse 220px 160px at 45% 75%, #8fdcfa 0%, transparent 100%),
      radial-gradient(ellipse 200px 160px at 90% 20%, #7ad3f6 0%, transparent 100%),
      linear-gradient(160deg, #6fd0f5 0%, var(--sky) 50%, var(--sky-deep) 100%);
  }
  .bitlume .panel-copy { left: 672px; top: 220px; width: 490px; color: var(--navy); }

  .site-footer { position: absolute; top: 2620px; left: 0; width: 1200px; height: 192px; background: var(--footer); color: var(--white); text-align: center; }
  .demo-title { font-size: 28px; font-weight: 500; padding-top: 24px; }
  .demo-button { display: inline-block; margin-top: 14px; padding: 7px 24px; background: var(--orange); color: var(--white); font-size: 18px; border-radius: 3px; text-decoration: none; }
  .copyright { position: absolute; left: 0; bottom: 0; width: 1200px; height: 52px; line-height: 52px; background: var(--footer-bar); font-size: 14px; color: #bbbbbb; }
</style>
</head>
<body>
  <header class="site-header">
    <div class="brand"><span class="brand-dot"></span>QUILLBARN</div>
    <nav class="main-nav">
      <a href="#">Home</a>
      <a href="#">What is Quillbarn</a>
      <a href="#">Codenest</a>
      <a href="#">Yellow Paper</a>
      <a href="#">Contact</a>
    </nav>
  </header>

  <section class="panel hero">
    <div class="hero-art" role="img" aria-label="Isometric illustration of blue data blocks and servers linked by network lines"></div>
    <div class="panel-copy hero-copy">
      <h1>QUILLBARN</h1>
      <p>A decentralized graph to exchange cryptocurrencies with no fee, no counterparty</p>
    </div>
  </section>

  <section class="panel peer">
    <div class="panel-art" role="img" aria-label="Illustration of red glowing cubes joined in a peer-to-peer network"></div>
    <div class="panel-copy">
      <h2>Peer-to-Peer<br>Decentralized Exchange</h2>
      <p>The ledger runs on a peer-to-peer network of computers that combined with cryptographic methods and algorithms realizes secure validation of transactions</p>
    </div>
  </section>

  <section class="panel fee">
    <div class="panel-art" role="img" aria-label="Pattern of yellow and white hexagons"></div>
    <div class="panel-copy">
      <h2>Exchange and transact<br>without paying a fee</h2>
      <p>Normally for trading currencies (real or virtual) you should pay a fee, however Quillbarn makes it possible to do transactions and exchanges with no fee</p>
    </div>
  </section>

  <section class="panel currencies">
    <div class="panel-art" role="img" aria-label="Dark illustration of currency symbols in circles around a central chip"></div>
    <div class="panel-copy">
      <h2>Represents (almost) all<br>Currencies</h2>
      <p>Bring (almost) any currency (real or virtual) into Quillbarn and work with all of them the same way</p>
    </div>
  </section>

  <section class="panel bitlume">
    <div class="panel-art" role="img" aria-label="Light blue illustration of a world network with coin nodes"></div>
    <div class="panel-copy">
      <h2>Fast and Fee-free<br>Bitlume Exchange</h2>
      <p>Bitlume is expensive and slow to trade, BUT in Quillbarn network you can trade or exchange Bitlume fast, without any fees.</p>
    </div>
  </section>

  <footer class="site-footer">
    <h3 class="demo-title">Request a demo of testnet</h3>
    <a class="demo-button" href="#">Send Email</a>
    <div class="copyright">© Copyright 2018 Quillbarn network</div>
  </footer>
</body>
</html>
```